We need a full corporate logo and stationary design for our business oxForge. OxForge provides 3D Printing Services to the Australian Market.

Our predominant market is the Mining and Architectural industries and our secondary market is the Entrepreneur / Start-up sector.

What we are after:

1. Logo
2. Business Card Design
3. Letterhead Design
4. Email Signature Design

File Formats we require in colour, greyscale and Black and White:

1 .AI
2 .EPS
3 .TIF
4 .PDF
5 .PNG (300 dpi)
6 .JPG (300 dpi)
7 .GIF (300 dpi)

• Should Not Have:
- "Clip-Art" should not be used.

```html
<!DOCTYPE html>
<html lang="en">
<head>
<meta charset="utf-8">
<title>oxForge – Business Card &amp; Letterhead</title>
<link rel="stylesheet" href="https://fonts.googleapis.com/css2?family=Cabin:wght@400&family=Open+Sans:wght@400;700&display=swap">
<style>
  :root {
    --page-bg: #ffffff;
    --paper: #ffffff;
    --charcoal: #404041;
    --charcoal-deep: #333334;
    --band-yellow: #f0bb1a;
    --brand-yellow: #e2a925;
    --title-grey: #6d7474;
    --card-white: #ffffff;
    --shadow: rgba(0, 0, 0, 0.28);
  }
  * { box-sizing: border-box; margin: 0; padding: 0; }
  html, body {
    width: 1200px;
    height: 1000px;
    overflow: hidden;
    background: var(--page-bg);
  }
  .presentation {
    position: relative;
    width: 1200px;
    height: 1000px;
    font-family: "Open Sans", Verdana, sans-serif;
  }
  .presentation-title {
    position: absolute;
    left: 719px;
    top: 82px;
    font-family: "Cabin", "Open Sans", sans-serif;
    font-weight: 400;
    font-size: 35px;
    letter-spacing: 0.2px;
    color: var(--title-grey);
    white-space: nowrap;
  }

  /* Brand lockup */
  .brand {
    position: absolute;
    display: flex;
    align-items: center;
  }
  .brand-mark {
    flex: none;
    background: var(--charcoal-deep);
  }
  .brand-text {
    display: flex;
    flex-direction: column;
  }
  .brand-name {
    font-family: "Open Sans", Verdana, sans-serif;
    font-weight: 700;
    color: var(--brand-yellow);
    line-height: 1;
  }
  .brand-tagline {
    font-family: "Open Sans", Verdana, sans-serif;
    font-weight: 400;
    color: var(--charcoal-deep);
    line-height: 1;
    white-space: nowrap;
  }

  /* Letterhead */
  .letterhead {
    position: absolute;
    left: 66px;
    top: 80px;
    width: 612px;
    height: 862px;
    background: var(--paper);
    box-shadow: 4px 6px 14px var(--shadow);
  }
  .letterhead .brand {
    right: 46px;
    top: 30px;
  }
  .letterhead .brand-mark {
    width: 42px;
    height: 60px;
    margin-right: 8px;
  }
  .letterhead .brand-name { font-size: 46px; letter-spacing: 0.5px; }
  .letterhead .brand-tagline { font-size: 11px; margin-top: 4px; text-align: right; }
  .letterhead-stripe {
    position: absolute;
    left: 0;
    right: 0;
    top: 770px;
    height: 16px;
    background: var(--band-yellow);
  }
  .letterhead-footer {
    position: absolute;
    left: 0;
    right: 0;
    top: 786px;
    bottom: 0;
    background: var(--charcoal);
    display: flex;
    align-items: center;
    justify-content: center;
  }
  .letterhead-web {
    font-size: 13px;
    color: var(--band-yellow);
    letter-spacing: 0.3px;
    margin-top: -4px;
  }

  /* Business card */
  .business-card {
    position: absolute;
    left: 780px;
    top: 202px;
    width: 286px;
    height: 179px;
    background: var(--charcoal);
    box-shadow: 4px 6px 14px var(--shadow);
    overflow: hidden;
  }
  .card-header {
    position: relative;
    height: 61px;
    background: var(--card-white);
  }
  .card-header .brand {
    right: 10px;
    top: 11px;
  }
  .card-header .brand-mark {
    width: 20px;
    height: 30px;
    margin-right: 5px;
  }
  .card-header .brand-name { font-size: 23px; letter-spacing: 0.3px; }
  .card-header .brand-tagline { font-size: 6px; margin-top: 2px; text-align: right; }
  .card-body {
    padding: 9px 0 0 20px;
  }
  .card-name {
    font-size: 13px;
    color: var(--card-white);
    line-height: 16px;
  }
  .card-role {
    font-size: 10px;
    color: var(--card-white);
    line-height: 13px;
  }
  .card-contacts {
    list-style: none;
    margin-top: 12px;
  }
  .card-contacts li {
    font-size: 10.5px;
    color: var(--band-yellow);
    line-height: 13.7px;
    white-space: nowrap;
  }
</style>
</head>
<body>
<main class="presentation">
  <h1 class="presentation-title">business card &amp; headletter</h1>

  <section class="letterhead" aria-label="Letterhead">
    <div class="brand">
      <span class="brand-mark"></span>
      <div class="brand-text">
        <span class="brand-name">oxForge</span>
        <span class="brand-tagline">3D Printing Services</span>
      </div>
    </div>
    <div class="letterhead-stripe"></div>
    <footer class="letterhead-footer">
      <span class="letterhead-web">www.oxforge.com.au</span>
    </footer>
  </section>

  <section class="business-card" aria-label="Business card">
    <header class="card-header">
      <div class="brand">
        <span class="brand-mark"></span>
        <div class="brand-text">
          <span class="brand-name">oxForge</span>
          <span class="brand-tagline">3D Printing Services</span>
        </div>
      </div>
    </header>
    <div class="card-body">
      <p class="card-name">Your Name</p>
      <p class="card-role">President</p>
      <ul class="card-contacts">
        <li>your_email@oxforge.com.au</li>
        <li>www.oxforge.com.au</li>
        <li>P&nbsp; 0123 456 789</li>
        <li>M 0123 456 789</li>
      </ul>
    </div>
  </section>
</main>
</body>
</html>
```